Harborline Tech Service, Technology & Security Co.

need a new business card design for our Technology & Security Company. We are a Computer Networking Company, Security Camera Installers, Phone Systems.

Target Market(s)

Construction, Medical, Law Offices, Accounting, Retail etc.

Industry/Entity Type

Information Technology

Logo is attached, colors are Blue, Red, Black. Blue for Technology & Red is for Security Cameras, Access Control, Alarm Systems

Colors
fbed22
ec1f27
0555a3
ffffff

Requirements
Must have
• Pictures or Icons for
• For Technology:
• Computer, Network, Phone System, Copier, TV, Cabling
• For Security:
• Video Surveillance, Access Control, Intercom, Fire Alarm, Burglar Alarm, Time Clock

```html
<!DOCTYPE html>
<html lang="en">
<head>
<meta charset="utf-8">
<title>Harborline Tech Service – Business Card</title>
<link href="https://fonts.googleapis.com/css2?family=Roboto:wght@400;700;900&family=Roboto+Condensed:wght@400;700&display=swap" rel="stylesheet">
<style>
  :root {
    --bg: #2b2b2b;
    --card: #f4f4f4;
    --ink: #1e1e1e;
    --text: #4a4a4a;
    --blue: #0e6fb8;
    --red: #e2231a;
    --band-red: #e63c26;
  }
  * { margin: 0; padding: 0; box-sizing: border-box; }
  html, body { width: 1200px; height: 960px; overflow: hidden; }
  body { background: var(--bg); font-family: "Roboto", sans-serif; position: relative; }

  .card {
    position: absolute;
    width: 600px;
    height: 343px;
    background: var(--card);
    overflow: hidden;
  }
  .card--front { left: 314px; top: 113px; }
  .card--back { left: 311px; top: 472px; }

  .brand {
    position: absolute;
    left: 0; right: 0;
    display: flex;
    justify-content: center;
    align-items: center;
    gap: 10px;
  }
  .card--front .brand { top: 80px; }
  .card--back .brand { top: 84px; }
  .brand__dot { width: 14px; height: 14px; border-radius: 50%; background: var(--blue); }
  .brand__name {
    font-family: "Roboto", sans-serif;
    font-weight: 900;
    font-size: 28px;
    letter-spacing: -0.3px;
    color: var(--ink);
  }

  .identity {
    position: absolute;
    right: 300px;
    top: 176px;
    text-align: right;
    line-height: 19px;
    color: var(--text);
    font-size: 14.5px;
  }
  .identity__name {
    font-family: "Roboto Condensed", sans-serif;
    font-size: 23px;
    color: var(--blue);
    line-height: 26px;
  }
  .identity__title {
    font-family: "Roboto Condensed", sans-serif;
    font-weight: 700;
    font-size: 16px;
    color: var(--red);
    line-height: 20px;
  }

  .contacts {
    position: absolute;
    left: 312px;
    top: 179px;
    list-style: none;
    font-size: 14.5px;
    line-height: 19px;
    color: var(--text);
  }
  .contacts__key { font-weight: 700; color: var(--blue); margin-right: 6px; }
  .contacts__key b { color: var(--red); font-weight: 700; }

  .band {
    position: absolute;
    left: 0; right: 0; bottom: 0;
    height: 30px;
    background: linear-gradient(to right, var(--blue) 0 480px, var(--band-red) 480px);
    color: #fff;
    font-size: 14px;
    letter-spacing: 2.6px;
    text-align: center;
    line-height: 30px;
    padding-right: 6px;
  }

  .services {
    position: absolute;
    left: 0; right: 0;
    top: 165px;
    text-align: center;
    color: var(--text);
    font-size: 14.5px;
    line-height: 18px;
  }
  .services__group + .services__group { margin-top: 12px; }
  .services__heading { font-weight: 700; font-size: 14.5px; line-height: 20px; }
  .services__heading--tech { color: var(--blue); }
  .services__heading--security { color: var(--red); }
  .sep { display: inline-block; width: 5px; height: 5px; border-radius: 50%; vertical-align: middle; margin: 0 3px; }
  .sep--tech { background: var(--blue); }
  .sep--security { background: var(--red); }
</style>
</head>
<body>

  <section class="card card--front" aria-label="Business card front">
    <div class="brand">
      <span class="brand__dot"></span>
      <span class="brand__name">HARBORLINE TECH SERVICE</span>
    </div>

    <div class="identity">
      <div class="identity__name">DANIEL REYES</div>
      <div class="identity__title">CEO/FOUNDER</div>
      <div>214 Birchwood Court</div>
      <div>Juneau, Alaska 99801</div>
    </div>

    <ul class="contacts">
      <li><span class="contacts__key"><b>(</b>P<b>)</b></span>555 210 4817</li>
      <li><span class="contacts__key"><b>(</b>C<b>)</b></span>555 362 9051</li>
      <li><span class="contacts__key"><b>(</b>F<b>)</b></span>555 748 2230</li>
      <li><span class="contacts__key"><b>(</b>E<b>)</b></span>daniel@HarborlineTech.com</li>
    </ul>

    <div class="band">www.HarborlineTech.com</div>
  </section>

  <section class="card card--back" aria-label="Business card back">
    <div class="brand">
      <span class="brand__dot"></span>
      <span class="brand__name">HARBORLINE TECH SERVICE</span>
    </div>

    <div class="services">
      <div class="services__group">
        <div class="services__heading services__heading--tech">FOR TECHNOLOGY</div>
        <div>Computer<span class="sep sep--tech"></span>Network<span class="sep sep--tech"></span>Phone System</div>
        <div>Copier<span class="sep sep--tech"></span>TV<span class="sep sep--tech"></span>Cabling</div>
      </div>
      <div class="services__group">
        <div class="services__heading services__heading--security">FOR SECURITY</div>
        <div>Video Surveillance<span class="sep sep--security"></span>Access Control<span class="sep sep--security"></span>Intercom</div>
        <div>Fire Alarm<span class="sep sep--security"></span>Burglar Alarm<span class="sep sep--security"></span>Time Clock</div>
      </div>
    </div>
  </section>

</body>
</html>
```